OV Holdings Invitation

I need an invitation designed for both online and hard copy distribution. I'm uploading a poorly designed online invitation that includes our logo and the blue and black colors we want to use. The online invitation must have an area to embed video (see attached).

With regard to the hard copy invitation, we need it to be a 5x7 card. Where the embedded video is on the online version, we would like you to create an image that represents the terms "monetizing innovation". If you go to www.ovhold.co, you can see what the company is using to express those words right now. There are no limitations to what you come up with for this visual.

Please note: The invitation both online and hardcopy must be designed so that all the information in the attached copy can be read. This includes: Logo, hosted by; When/date, where, two quotes, etc.

I've attached our logo files. You can use whichever logo file you want for your design.

Many thanks...looking forward to seeing all your great designs.
Updates

All - you do not need to follow our format for the invite as long as all the information we need is on it....Note:  we will need to be able to edit the information for other presentation.

EPS files of the logo have been added for those of you who have requested it.

Many thanks,

Marta

Reason: All, Apologies for the extension. The decision-makers have been travelling and have not had a chance to thoroughly review the designs. We really appreciate your patience. Many thanks, Marta

Target Market(s)

Investors and Media

Industry/Entity Type

It Company

Requirements
Must have
• Please use the blue and black colors as seen in the attached uploaded files.

```html
<!DOCTYPE html>
<html lang="en">
<head>
<meta charset="utf-8">
<title>OV Holdings – Monetizing Innovation</title>
<link rel="stylesheet" href="https://fonts.googleapis.com/css2?family=Arimo:wght@400;700&family=Open+Sans:wght@400;600&display=swap">
<style>
  :root {
    --brand-blue: #1c5f99;
    --brand-blue-deep: #174f82;
    --ink-blue: #1f5a9a;
    --accent-orange: #f5a623;
    --accent-green: #3cb54a;
    --muted-grey: #7d7d7d;
    --ink: #1e1e1e;
    --paper: #ffffff;
  }
  * { margin: 0; padding: 0; box-sizing: border-box; }
  html, body { width: 1200px; height: 927px; overflow: hidden; background: var(--paper); }
  .invite { position: relative; width: 1200px; height: 927px; font-family: "Arimo", Arial, sans-serif; overflow: hidden; }

  .header-band { position: absolute; left: 0; top: 0; width: 1200px; height: 173px;
    background: linear-gradient(180deg, #2a6ea8 0%, var(--brand-blue) 100%); }
  .header-artwork { position: absolute; left: 180px; top: 0; width: 1020px; height: 173px;
    background: linear-gradient(90deg, rgba(255,255,255,0) 0%, rgba(160,195,230,0.28) 45%, rgba(120,190,140,0.35) 100%); }
  .head-figure { position: absolute; left: 22px; top: 0; width: 170px; height: 215px;
    background: linear-gradient(180deg, rgba(120,170,215,0.55) 0%, rgba(60,120,180,0.85) 100%); }
  .event-title { position: absolute; left: 0; width: 1200px; top: 36px; text-align: center;
    color: #fff; font-weight: 700; font-size: 42px; letter-spacing: 0.5px;
    text-shadow: 2px 2px 2px rgba(0,0,0,0.55); }
  .presented-by { position: absolute; left: 0; width: 1200px; top: 124px; text-align: center;
    color: var(--accent-orange); font-weight: 700; font-size: 23px; }

  .company-mark { position: absolute; left: 482px; top: 182px; width: 240px; height: 64px;
    display: flex; align-items: center; gap: 14px; }
  .company-mark .mark-square { width: 40px; height: 40px; background: var(--brand-blue-deep); }
  .company-mark .mark-name { font-weight: 700; font-size: 26px; color: var(--brand-blue-deep); }

  .video-headline { position: absolute; left: 303px; top: 262px; color: var(--ink-blue);
    font-weight: 700; font-size: 25px; }
  .video-frame { position: absolute; left: 221px; top: 397px; width: 369px; height: 277px;
    background: #000; padding: 14px 0 28px; }
  .video-still { width: 100%; height: 100%;
    background: linear-gradient(120deg, #3a4fb0 0%, #6f86d8 40%, #c9c3b8 70%, #d8b060 100%); }
  .play-button { position: absolute; left: 11px; bottom: 4px; }
  .video-description { position: absolute; left: 38px; width: 736px; top: 682px; text-align: center;
    font-family: "Open Sans", Arial, sans-serif; color: var(--ink-blue); font-size: 24px; line-height: 33px; }

  .details { position: absolute; left: 775px; width: 420px; top: 0; }
  .details p { position: absolute; left: 0; width: 420px; text-align: center; white-space: nowrap; }
  .strong-blue { color: var(--ink-blue); font-weight: 700; font-size: 22px; text-shadow: 1px 1px 1px rgba(0,0,0,0.35); }
  .strong-grey { color: var(--muted-grey); font-weight: 700; font-size: 22px; text-shadow: 1px 1px 1px rgba(0,0,0,0.35); }
  .plain { color: var(--ink); font-family: "Open Sans", Arial, sans-serif; font-size: 18px; }
  .host { color: var(--ink-blue); font-weight: 700; font-size: 19px; text-shadow: 1px 1px 1px rgba(0,0,0,0.3); }
  .dot { display: inline-block; width: 14px; height: 14px; border-radius: 50%;
    background: var(--accent-green); margin-right: 3px; vertical-align: 0; }

  .footer-band { position: absolute; left: 0; top: 851px; width: 1200px; height: 76px; background: var(--brand-blue); }
  .footer-note { position: absolute; left: 59px; top: 865px; color: #fff;
    font-family: "Open Sans", Arial, sans-serif; font-size: 18px; }
  .footer-url { position: absolute; left: 858px; top: 859px; color: #fff; font-weight: 700; font-size: 32px; }
</style>
</head>
<body>
<main class="invite">
  <div class="header-band"></div>
  <div class="header-artwork" role="img" aria-label="Flowing light waves with green bubbles and a bright sun across the header"></div>
  <div class="head-figure" role="img" aria-label="Profile of a head with money gears inside, symbolising monetized ideas"></div>

  <h1 class="event-title">Monetizing Innovation</h1>
  <p class="presented-by">A Special Presentation Of:</p>

  <div class="company-mark">
    <span class="mark-square"></span>
    <span class="mark-name">OV Holdings</span>
  </div>

  <h2 class="video-headline">Video Headline</h2>
  <div class="video-frame">
    <div class="video-still" role="img" aria-label="Video still of a news van in motion"></div>
    <svg class="play-button" width="28" height="26" viewBox="0 0 28 26" aria-hidden="true">
      <rect x="1" y="1" width="26" height="24" rx="3" fill="#222" stroke="#bbb" stroke-width="1.5"/>
      <path d="M10 7 L20 13 L10 19 Z" fill="#ddd"/>
    </svg>
  </div>
  <p class="video-description">Description of Video and so on and so on and so on with just a little bit more here and even more if necessary</p>

  <section class="details">
    <p class="strong-blue" style="top:263px"><span class="dot"></span>Wednesday, September 28th</p>
    <p class="strong-grey" style="top:292px">Check-In 3:00 pm</p>
    <p class="strong-grey" style="top:321px">Presentation 3:30 - 4:30 pm</p>

    <p class="strong-blue" style="top:379px">Harbor Lodge – Cypress Room</p>
    <p class="strong-grey" style="top:408px">2150 Harbor Lodge Way</p>
    <p class="strong-grey" style="top:437px">Lakeview CA 92507</p>

    <p class="plain" style="top:493px"><span class="dot"></span>Please RSVP by</p>
    <p class="strong-blue" style="top:521px">Monday, September 26th</p>
    <p class="plain" style="top:548px">Dana Whitfield</p>
    <p class="strong-grey" style="top:576px">(877) 555-0142 x1003</p>
    <p class="strong-grey" style="top:604px">dwhitfield@ovhold.co</p>

    <p class="plain" style="top:662px"><span class="dot"></span>Hosted By:</p>
    <p class="host" style="top:699px">Ravi Osterman, CEO</p>
    <p class="host" style="top:724px">Glen Marlow, President</p>
    <p class="host" style="top:749px">Luis Ortega, CFO</p>
    <p class="host" style="top:774px">Tom Keller, COO</p>
    <p class="host" style="top:800px">Evan Briggs, CCO</p>
  </section>

  <footer class="footer-band"></footer>
  <p class="footer-note">*Please note that you must be an accredited investor to attend the presentation</p>
  <p class="footer-url">www.ovhold.co</p>
</main>
</body>
</html>
```